" Plataforma digital que empresas podem usar para dar acesso a seus funcionarios a benefícios relacionados com cuidado e educação de crianças ate 5 anos: desde dicas praticas, sugestão de produtos, referencias de prestadores de serviços ate produtos financeiros - tudo relacionado com esta etapa da vida. "

```html
<!DOCTYPE html>
<html lang="pt-BR">
<head>
<meta charset="utf-8">
<title>Pimpolho — Papel timbrado</title>
<link href="https://fonts.googleapis.com/css2?family=Nunito:wght@400;600;800&display=swap" rel="stylesheet">
<style>
  :root {
    --backdrop: #d9dadc;
    --paper: #ffffff;
    --brand-orange: #f07a1a;
    --text-body: #5a5a5a;
    --text-muted: #8a8a8a;
    --signature-tone: #e6e6e6;
  }
  html, body {
    margin: 0;
    width: 1200px;
    height: 1200px;
    overflow: hidden;
    background: var(--backdrop);
    font-family: "Nunito", sans-serif;
  }
  .letterhead {
    position: absolute;
    left: 210px;
    top: 50px;
    width: 780px;
    height: 1100px;
    background: var(--paper);
    box-sizing: border-box;
    padding: 70px 80px 0;
    box-shadow: 0 2px 10px rgba(0,0,0,0.08);
  }
  .brand-name {
    position: absolute;
    top: 64px;
    right: 80px;
    margin: 0;
    font-size: 54px;
    font-weight: 800;
    color: var(--brand-orange);
    letter-spacing: 0.5px;
  }
  .letter-body {
    position: absolute;
    top: 200px;
    left: 80px;
    right: 80px;
    font-size: 15px;
    line-height: 1.8;
    color: var(--text-body);
    text-align: justify;
  }
  .letter-body p { margin: 0 0 20px; }
  .contact-block {
    position: absolute;
    left: 80px;
    bottom: 80px;
    font-size: 12px;
    color: var(--text-muted);
  }
  .social-row { display: flex; gap: 6px; margin-bottom: 12px; }
  .social-row span {
    width: 16px; height: 16px;
    background: var(--brand-orange);
  }
  .contact-line {
    display: flex;
    align-items: center;
    gap: 8px;
    margin-bottom: 6px;
  }
  .contact-line svg { width: 16px; height: 16px; flex: none; }
  .closing {
    position: absolute;
    left: 380px;
    bottom: 80px;
    font-size: 13px;
    color: var(--text-muted);
  }
  .closing .signature {
    width: 150px;
    height: 50px;
    margin: 10px 0;
    background: linear-gradient(90deg, var(--signature-tone), #f4f4f4);
  }
  .closing .signer { color: var(--text-body); font-weight: 600; }
  .footer-band {
    position: absolute;
    left: 0; right: 0; bottom: 0;
    height: 14px;
    background: var(--brand-orange);
  }
</style>
</head>
<body>
  <main class="letterhead">
    <h1 class="brand-name">Pimpolho</h1>

    <section class="letter-body">
      <p>Prezada equipe, é com alegria que apresentamos a nova plataforma de benefícios para famílias com crianças pequenas. Reunimos dicas práticas, produtos selecionados e profissionais de confiança em um só lugar, pensados para apoiar cada etapa dos primeiros anos.</p>
      <p>Sua empresa pode oferecer aos colaboradores acesso simples a cuidados, educação e soluções financeiras para filhos de até cinco anos. Tudo isso com acompanhamento próximo, conteúdo confiável e atendimento humano.</p>
      <p>Ficaremos felizes em apresentar os detalhes em uma conversa. Conte conosco para cuidar de quem cuida.</p>
    </section>

    <address class="contact-block">
      <div class="social-row"><span></span><span></span><span></span><span></span></div>
      <div class="contact-line">
        <svg viewBox="0 0 16 16"><rect width="16" height="16" fill="var(--brand-orange)"/><path d="M5 4h2l1 2.5-1.2.8a6 6 0 0 0 2 2l.8-1.2L12 9v2a1 1 0 0 1-1 1A7 7 0 0 1 4 5a1 1 0 0 1 1-1z" fill="#fff"/></svg>
        +55 11 4000-1234
      </div>
      <div class="contact-line">
        <svg viewBox="0 0 16 16"><rect width="16" height="16" fill="var(--brand-orange)"/><rect x="3.5" y="5" width="9" height="6" fill="none" stroke="#fff"/><path d="M3.5 5l4.5 3.5L12.5 5" fill="none" stroke="#fff"/></svg>
        contato@pimpolho.com.br
      </div>
      <div class="contact-line">
        <svg viewBox="0 0 16 16"><rect width="16" height="16" fill="var(--brand-orange)"/><circle cx="8" cy="8" r="4.5" fill="none" stroke="#fff"/><path d="M3.5 8h9M8 3.5c-2 2.5-2 6.5 0 9M8 3.5c2 2.5 2 6.5 0 9" fill="none" stroke="#fff" stroke-width="0.8"/></svg>
        www.pimpolho.com.br
      </div>
      <div class="contact-line">
        <svg viewBox="0 0 16 16"><rect width="16" height="16" fill="var(--brand-orange)"/><path d="M8 13s-3.5-3.8-3.5-6.3a3.5 3.5 0 0 1 7 0C11.5 9.2 8 13 8 13z" fill="#fff"/><circle cx="8" cy="6.7" r="1.2" fill="var(--brand-orange)"/></svg>
        Rua das Flores, 120, São Paulo
      </div>
    </address>

    <div class="closing">
      <div>Atenciosamente,</div>
      <div class="signature" role="img" aria-label="Assinatura manuscrita"></div>
      <div class="signer">Marina Costa</div>
      <div>Diretora</div>
    </div>

    <div class="footer-band"></div>
  </main>
</body>
</html>
```